BRIGHTVALE ADVISERS POWERPOINT PRESENTATION TEMPLATE 1

We need the ultimate quality Powerpoint presentation design.
We are the advisory firm working with modern world class tech companies throughout Europe, their founders, shareholders, and potential investors.
The new template must contain elements such as our logo, appropriate backgrounds, be at the same time very attractive visually and easy to rear. Also there must be some place where logo of our clients should be placed.

We like:
- icons and
- infographics,
so attractive design in this area will be greatly appreciated.

Please avoid serif fonts and excessive decorations such as "waves" or other similar decor.

We are also in contact with serious investors - wealthy individuals, reputable financial institutions, and their advisers; banks, private equity investors, global technology companies.

The Powerpoint template design must send a message that:
- we are a high technology oriented team of professionals,
- we provide modern financial advisory services
- but at the same time we are open minded, creative, yet very competent in the area of corporate finance.

The Powerpoint template must complement our business card design, first impression of a team of top notch professionals who advise top notch tech companies on their top notch corporate finance and M&A projects.

Enclosed are sets of our logo, current template, business card project which won previous competition.

It is perhaps a good basis to start with and get us to the template of our dreams.

While working on this project please think about the following firms which at some point may be looking at your design:
- Quorlin
- Tavindex
- Pelorim
- Veskaran (Zundle)
- Marowisp
- Turnequo
- Dovrash
- Kelvaro
- Obrethy

The quality of the design, its style, aesthetics must meet the top criteria in contemporary design trends.

Target Market(s)

Banks, financial investors, strategic investors

Industry/Entity Type

Finance

Font styles to use
Sans Serif

Requirements
Must have
• Icons
Infographics
Attractive backgrounds
Clean design
Harmonize with logo and emblem colors.
Should not have
• Excessive tacky decor (waves, etc)
Serif fonts
Excessive colors

```html
<!DOCTYPE html>
<html lang="en">
<head>
<meta charset="utf-8">
<title>Brightvale Advisers – Presentation Slides</title>
<link rel="stylesheet" href="https://fonts.googleapis.com/css2?family=Roboto:ital,wght@0,300;0,400;0,500;0,700;1,400;1,700&display=swap">
<style>
  :root{
    --navy:#0e2a4f;
    --navy-dark:#1c2b55;
    --band:#d4e3f2;
    --band-grey:#e4e9f0;
    --band-pale:#eff2f6;
    --rule:#8fb1d6;
    --bar-light:#9dc7e6;
    --table-head:#5b9bd5;
    --table-cell:#cfdeef;
    --text:#222;
    --muted:#555;
    --green:#1f9a56;
    --green-dark:#0b5a33;
  }
  *{box-sizing:border-box;margin:0;padding:0}
  html,body{width:1200px;height:1200px;overflow:hidden;background:#fff;font-family:"Roboto",Arial,sans-serif;color:var(--text)}
  .stage{position:absolute;left:0;top:0;width:1920px;height:1920px;transform:scale(.625);transform-origin:0 0}
  .slide{position:absolute;background:#fff;border:2px solid #cfcfcf;box-shadow:0 1px 3px rgba(0,0,0,.12);overflow:hidden}
  .slide > *{position:absolute}
  .band{background:var(--band)}
  .band-grey{background:var(--band-grey)}
  .band-pale{background:var(--band-pale)}
  .slide-title{font-weight:700;color:var(--navy);letter-spacing:.5px;white-space:nowrap}
  .section-title{font-weight:700;color:var(--navy);font-size:16px;white-space:nowrap}
  .rule-v{width:2px;background:var(--rule)}
  .rule-h{height:1.5px;background:var(--rule)}
  .footnote{font-size:10px;font-weight:700;font-style:italic;color:var(--text)}
  .brand{display:flex;flex-direction:column;align-items:center;gap:6px}
  .brand-dot{width:30px;height:30px;border-radius:50%;background:#2f5f9e}
  .brand-name{font-size:21px;font-weight:400;color:#1c3f72;letter-spacing:-.5px}
  .arrow-list{list-style:none}
  .arrow-list li{position:relative}
  .arrow-list li::before{content:"→";position:absolute;font-weight:700}
  /* slide one */
  .s1{left:398px;top:246px;width:1140px;height:644px}
  .commentary-title{font-size:15px;font-weight:500;color:var(--text)}
  .commentary{font-size:10.5px;line-height:15.5px;color:var(--muted);text-align:justify}
  .commentary .arrow-list li::before{left:-38px}
  .commentary .sub{list-style:none;padding-left:57px}
  .commentary .sub li{position:relative}
  .commentary .sub li::before{content:"◆";position:absolute;left:-35px;font-size:6px}
  .fin-table{border-collapse:separate;border-spacing:2px;font-size:8px}
  .fin-table th{background:var(--table-head);color:#fff;font-weight:700;height:31px;padding:0 8px;text-align:center}
  .fin-table th:first-child{text-align:left;width:106px}
  .fin-table td{background:var(--table-cell);height:32px;width:46px;padding:0 8px;color:var(--text)}
  /* slide two */
  .s2{left:555px;top:966px;width:1106px;height:621px}
  .story{font-size:16px;line-height:19.5px;color:var(--muted)}
  .story em{display:block;margin-top:19px;font-weight:700}
  .history{font-size:14px;line-height:19.5px;color:var(--text);text-align:justify}
  .history .arrow-list li::before{left:-40px}
  .milestone{font-size:12px;line-height:14.5px;color:var(--text)}
  .milestone b{display:block}
  .year{font-size:19px;font-weight:700;color:var(--text)}
</style>
</head>
<body>
<div class="stage">

  <!-- Slide: Basic Information -->
  <section class="slide s1">
    <div class="band-grey" style="left:0;top:0;width:122px;height:84px"></div>
    <div class="band-pale" style="left:0;top:84px;width:122px;height:34px"></div>
    <div class="band" style="left:122px;top:0;width:602px;height:84px"></div>
    <div class="band" style="left:560px;top:62px;width:580px;height:64px"></div>
    <h1 class="slide-title" style="left:167px;top:22px;font-size:52px">Basic Information</h1>
    <h2 class="section-title" style="left:168px;top:98px">Key financial results, PLNm</h2>
    <h2 class="section-title" style="left:582px;top:98px">Average Revenue User, PLN</h2>
    <div class="rule-v" style="left:546px;top:94px;height:448px"></div>

    <svg style="left:0;top:0" width="560" height="360" viewBox="0 0 560 360" font-family="Roboto, sans-serif" font-size="8" fill="#333">
      <g fill="var(--bar-light)">
        <rect x="86" y="284" width="24" height="16"/>
        <rect x="181" y="264" width="22" height="36"/>
        <rect x="276" y="238" width="21" height="62"/>
        <rect x="370" y="224" width="22" height="76"/>
        <rect x="465" y="217" width="22" height="83"/>
      </g>
      <g fill="var(--navy-dark)">
        <rect x="116" y="302" width="24" height="2"/>
        <rect x="306" y="295" width="22" height="5"/>
        <rect x="400" y="292" width="23" height="8"/>
        <rect x="494" y="289" width="24" height="11"/>
      </g>
      <polyline points="113,210 207,187 302,171 396,166 491,161" fill="none" stroke="#999" stroke-width="1.2" stroke-dasharray="2 2"/>
      <g fill="#999"><circle cx="113" cy="210" r="2.2"/><circle cx="207" cy="187" r="2.2"/><circle cx="302" cy="171" r="2.2"/><circle cx="396" cy="166" r="2.2"/><circle cx="491" cy="161" r="2.2"/></g>
      <text x="119" y="201">-13.33%</text><text x="213" y="179">0.00%</text><text x="308" y="163">9.00%</text><text x="403" y="158">11.29%</text><text x="498" y="153">14.71%</text>
      <text x="86" y="279">15.00</text><text x="180" y="259">30.00</text><text x="275" y="234">50.00</text><text x="369" y="220">62.00</text><text x="464" y="212">68.00</text>
      <text x="118" y="314">2.00</text><text x="216" y="297">.00</text><text x="307" y="291">4.50</text><text x="403" y="288">7.00</text><text x="494" y="284">10.00</text>
      <line x1="66" y1="307" x2="535" y2="307" stroke="#ccc"/>
      <text x="101" y="320">20XX</text><text x="196" y="320">20XX</text><text x="291" y="320">20XX</text><text x="385" y="320">20XX</text><text x="480" y="320">20XX</text>
      <rect x="152" y="324" width="6" height="6" fill="var(--bar-light)"/><text x="163" y="330">Revenue</text>
      <rect x="273" y="324" width="6" height="6" fill="var(--navy-dark)"/><text x="284" y="330">EBITDA</text>
      <circle cx="396" cy="327" r="2.2" fill="#999"/><text x="404" y="330">EBITDA margin</text>
      <line x1="168" y1="348" x2="535" y2="348" stroke="var(--rule)" stroke-width="1.5"/>
    </svg>

    <h3 class="commentary-title" style="left:102px;top:369px">Commentary</h3>
    <div class="commentary" style="left:102px;top:402px;width:432px">
      <ul class="arrow-list">
        <li>Between 20XX and 20XX the Company reported a dynamic growth, increasing the net profit margin from xx% to xx%</li>
        <li>Year 20XX is considered as a transition period for the Company, in which:
          <ul class="sub">
            <li>One-time expenses and other, less significant changes in costs occurred</li>
            <li>The Company started to integrate product portfolio</li>
            <li>To maintain high standards of services during COVID-19</li>
            <li>Thanks to the financing obtained, cooperation with economically stable companies, as well as active development, company is forecasted to return to a natural, fast development, strengthening its market-leading position.</li>
          </ul>
        </li>
      </ul>
    </div>

    <svg style="left:580px;top:135px" width="470" height="150" viewBox="580 135 470 150" font-family="Roboto, sans-serif" font-size="7" fill="#333">
      <text x="762" y="150" font-size="8">Average Revenue User, PLN</text>
      <polyline points="598,243 636,230 674,223 712,214 750,204 788,196 826,193 864,188 902,185 940,181 978,179 1016,177 1024,177" fill="none" stroke="#b7d6ee" stroke-width="2"/>
      <polyline points="712,252 750,200 788,192 826,187 872,173 910,190 948,173 988,173 1024,172" fill="none" stroke="#2c3e66" stroke-width="2"/>
      <text x="598" y="237">30.00</text><text x="636" y="222">60.00</text><text x="674" y="216">70.00</text><text x="712" y="214">75.00</text>
      <text x="748" y="205">85.00</text><text x="786" y="203">100.00</text><text x="786" y="221">64.20</text><text x="824" y="199">110.00</text>
      <text x="860" y="187">130.00</text><text x="898" y="182">145.00</text><text x="898" y="199">107.00</text><text x="936" y="182">145.00</text>
      <text x="936" y="189">128.40</text><text x="974" y="178">155.00</text><text x="1012" y="170">171.30</text>
      <line x1="588" y1="255" x2="1042" y2="255" stroke="#bbb"/>
      <g font-size="7"><text x="598" y="267">20XX</text><text x="636" y="267">20XX</text><text x="674" y="267">20XX</text><text x="712" y="267">20XX</text><text x="750" y="267">20XX</text><text x="788" y="267">20XX</text><text x="826" y="267">20XX</text><text x="864" y="267">20XX</text><text x="902" y="267">20XX</text><text x="940" y="267">20XX</text><text x="978" y="267">20XX</text><text x="1016" y="267">20XX</text></g>
      <line x1="656" y1="276" x2="664" y2="276" stroke="#b7d6ee" stroke-width="2"/><text x="669" y="279">Country 1</text>
      <line x1="792" y1="276" x2="800" y2="276" stroke="#ccc" stroke-width="2"/><text x="804" y="279">Country 2</text>
      <line x1="926" y1="276" x2="934" y2="276" stroke="#2c3e66" stroke-width="2"/><text x="938" y="279">Country 3</text>
    </svg>

    <table class="fin-table" style="left:602px;top:314px">
      <thead><tr><th>Financial Results PLNm</th><th>2015</th><th>2016</th><th>2017</th><th>2018</th><th>2019</th><th>2020</th></tr></thead>
      <tbody>
        <tr><td>Revenues</td><td>XXX</td><td></td><td></td><td></td><td></td><td></td></tr>
        <tr><td>Adj. EBITDA</td><td></td><td></td><td></td><td></td><td></td><td></td></tr>
        <tr><td>Adj. EBITDA margin</td><td></td><td></td><td></td><td></td><td></td><td></td></tr>
        <tr><td>Profit before tax</td><td>xx%</td><td></td><td></td><td></td><td></td><td></td></tr>
        <tr><td>Net income</td><td></td><td></td><td></td><td></td><td></td><td></td></tr>
        <tr><td>Net debt</td><td></td><td></td><td></td><td></td><td></td><td></td></tr>
      </tbody>
    </table>

    <div class="rule-h" style="left:95px;top:574px;width:898px"></div>
    <p class="footnote" style="left:110px;top:588px">Strictly confidential</p>
    <div class="brand" style="left:960px;top:562px">
      <span class="brand-dot"></span><span class="brand-name">BRIGHTVALE</span>
    </div>
  </section>

  <!-- Slide: Business Development -->
  <section class="slide s2">
    <div class="band-grey" style="left:0;top:0;width:120px;height:80px"></div>
    <div class="band-pale" style="left:0;top:80px;width:120px;height:32px"></div>
    <div class="band" style="left:120px;top:0;width:582px;height:80px"></div>
    <div class="band" style="left:545px;top:58px;width:561px;height:62px"></div>
    <h1 class="slide-title" style="left:163px;top:20px;font-size:50px">Business Development</h1>
    <h2 class="section-title" style="left:167px;top:93px">Business Story</h2>
    <div class="rule-h" style="left:165px;top:111px;width:348px"></div>
    <h2 class="section-title" style="left:566px;top:93px">Development History</h2>
    <div class="rule-v" style="left:530px;top:88px;height:246px"></div>

    <div class="story" style="left:167px;top:134px;width:340px">
      Lorem ipsum dolor sit amet, consectetur adipiscing elit.<br>
      Proin justo dui, elementum sed volutpat at, varius at nisl. Vestibulum sed aliquam tellus. Donec imperdiet lacus sed nunc efficitur, eget varius libero consequat.
      <em>Integer posuere sodales magna, rhoncus pharetra erat tempor eu.</em>
    </div>

    <div class="history" style="left:609px;top:131px;width:414px">
      <ul class="arrow-list">
        <li>The company was registered [...] . The first product, sold in [...]. Since the beginning of its activity, the Company has undertaken [...].</li>
        <li>The company started its activity from offering services [...]</li>
        <li>Responding to the market needs of the Company's Management Board, [...]</li>
        <li>The Management Board also decided on a geographical expansion into new, prospective markets [...]</li>
      </ul>
    </div>

    <div class="rule-h" style="left:93px;top:326px;width:987px"></div>
    <h2 class="section-title" style="left:167px;top:341px;font-size:15px">History and Milestones</h2>

    <svg style="left:0;top:0" width="1106" height="560" viewBox="0 0 1106 560">
      <rect x="173" y="449" width="130" height="12" fill="var(--green)"/>
      <rect x="303" y="449" width="129" height="12" fill="var(--green-dark)"/>
      <rect x="432" y="449" width="130" height="12" fill="var(--green)"/>
      <rect x="562" y="449" width="130" height="12" fill="var(--green-dark)"/>
      <rect x="692" y="449" width="130" height="12" fill="var(--green)"/>
      <rect x="822" y="449" width="178" height="12" fill="var(--green-dark)"/>
      <g stroke="#111" stroke-width="1.5">
        <line x1="173" y1="425" x2="173" y2="455"/><line x1="432" y1="425" x2="432" y2="455"/><line x1="692" y1="425" x2="692" y2="455"/>
        <line x1="303" y1="455" x2="303" y2="485"/><line x1="562" y1="455" x2="562" y2="485"/><line x1="822" y1="455" x2="822" y2="485"/>
      </g>
      <g fill="#111">
        <circle cx="173" cy="425" r="4.5"/><circle cx="432" cy="425" r="4.5"/><circle cx="692" cy="425" r="4.5"/>
        <circle cx="303" cy="485" r="4.5"/><circle cx="562" cy="485" r="4.5"/><circle cx="822" cy="485" r="4.5"/>
      </g>
    </svg>

    <span class="year" style="left:281px;top:421px">20XX</span>
    <span class="year" style="left:540px;top:421px">20XX</span>
    <span class="year" style="left:799px;top:421px">20XX</span>
    <span class="year" style="left:152px;top:473px">20XX</span>
    <span class="year" style="left:411px;top:473px">20XX</span>
    <span class="year" style="left:670px;top:473px">20XX</span>

    <p class="milestone" style="left:183px;top:369px;width:130px"><b>Vestibulum congue</b>Lorem ipsum dolor sit amet, consectetur adipiscing.</p>
    <p class="milestone" style="left:451px;top:364px;width:130px"><b>Vestibulum congue tempus</b>Lorem ipsum dolor sit amet.</p>
    <p class="milestone" style="left:702px;top:369px;width:190px"><b>Vestibulum congue tempus</b>Lorem ipsum dolor sit amet, consectetur adipiscing elit, sed.</p>
    <p class="milestone" style="left:219px;top:493px;width:170px"><b>Vestibulum congue</b>Lorem ipsum dolor sit amet, consectetur adipiscing.</p>
    <p class="milestone" style="left:570px;top:477px;width:130px"><b>Vestibulum</b>Lorem ipsum dolor sit amet, consectetur adipiscing elit.</p>
    <p class="milestone" style="left:839px;top:475px;width:170px"><b>Vestibulum congue tempus</b>Lorem ipsum dolor sit amet, consectetur</p>

    <div class="rule-h" style="left:93px;top:553px;width:872px"></div>
    <p class="footnote" style="left:107px;top:567px">Strictly confidential</p>
    <div class="brand" style="left:932px;top:540px">
      <span class="brand-dot"></span><span class="brand-name">BRIGHTVALE</span>
    </div>
  </section>

</div>
</body>
</html>
```